Great Opportunity !! Masters in Business Analytics College Course

the size is Full Page, with bleed*
8”x 10.75" plus 0.25" bleed.
please leave one inch for footer
the purpose is attract students to join this college program .
this is for students in USA .
college age of around 24 years old
I am looking for a flyer that is unique and shows creativity .
A flyer that people would want to look at it because it is unique.
you can choose either vector, text ,or picture.
if you do picture it should be a white USA citizen wearing a white solid shirt and not long hair

Target Market(s)

USA students about 23 in age to join this college program

Industry/Entity Type

education

Colors
0054AA
0677BA
7BADD7
CADEEF
E8F1F8
0094D4
00A9DD
6FCCEA
C7EBF8
E9F6FB

Requirements
Must have
• the text should not be crowded .. .. .. the ad should not be full of text
Should not have
• not have very large text .. it should not be a flyer that is full of text .. you have to figure out how to avoid looking at the ad and it is very busy with text

```html
<!DOCTYPE html>
<html lang="en">
<head>
<meta charset="utf-8">
<title>Master's in Business Analytics – Open House Flyer</title>
<link rel="stylesheet" href="https://fonts.googleapis.com/css2?family=Bebas+Neue&family=Inter:wght@400;500;700&display=swap">
<style>
  :root {
    --blue-deep: #0054AA;
    --blue-mid: #0677BA;
    --blue-bright: #0094D4;
    --blue-soft: #7BADD7;
    --blue-pale: #CADEEF;
    --blue-mist: #E8F1F8;
    --white: #ffffff;
    --stage: #eef0f2;
    --heading-font: "Bebas Neue", "Oswald", sans-serif;
    --body-font: "Inter", "Helvetica Neue", Arial, sans-serif;
  }
  * { box-sizing: border-box; margin: 0; padding: 0; }
  html, body {
    width: 1200px;
    height: 1200px;
    overflow: hidden;
    background: var(--stage);
  }
  .canvas {
    position: relative;
    width: 1200px;
    height: 1200px;
  }
  .flyer {
    position: absolute;
    left: 210px;
    top: 80px;
    width: 609px;
    height: 812px;
    transform: scale(1.28);
    transform-origin: top left;
    overflow: hidden;
    background: linear-gradient(90deg, var(--blue-deep) 0%, var(--blue-mid) 55%, var(--blue-bright) 100%);
    font-family: var(--body-font);
    color: var(--white);
  }
  .flyer-shapes {
    position: absolute;
    inset: 0;
    width: 609px;
    height: 812px;
  }
  .headline {
    position: absolute;
    left: 40px;
    top: 44px;
    font-family: var(--heading-font);
    font-weight: 400;
    font-size: 38px;
    line-height: 50px;
    letter-spacing: 0.3px;
    color: var(--white);
  }
  .copy {
    position: absolute;
    left: 40px;
    font-size: 11px;
    line-height: 16px;
    color: var(--white);
  }
  .intro { top: 178px; }
  .salary { top: 228px; }
  .source { top: 282px; }
  .band-list {
    position: absolute;
    left: 40px;
    top: 334px;
    font-size: 13.5px;
    line-height: 17px;
    color: var(--blue-deep);
    list-style: none;
  }
  .hired-title {
    position: absolute;
    left: 40px;
    top: 415px;
    font-size: 12.5px;
    font-weight: 700;
    color: var(--blue-deep);
    letter-spacing: 0.2px;
  }
  .employers { top: 432px; }
  .open-house-title {
    position: absolute;
    left: 40px;
    top: 546px;
    font-size: 20px;
    font-weight: 700;
    letter-spacing: 0.3px;
  }
  .event { top: 568px; font-size: 11.5px; }
  .accreditation { top: 616px; font-size: 11px; }
  .program-facts {
    position: absolute;
    left: 40px;
    top: 666px;
    font-size: 13.5px;
    line-height: 17.5px;
  }
</style>
</head>
<body>
<main class="canvas">
  <article class="flyer">
    <svg class="flyer-shapes" viewBox="0 0 609 812" xmlns="http://www.w3.org/2000/svg">
      <defs>
        <radialGradient id="photo-tone" cx="50%" cy="45%" r="60%">
          <stop offset="0%" stop-color="#f4f2f0"/>
          <stop offset="45%" stop-color="#e6dcd2"/>
          <stop offset="80%" stop-color="#cfd6de"/>
          <stop offset="100%" stop-color="#b8c4cf"/>
        </radialGradient>
      </defs>
      <circle class="ring-outer" cx="640" cy="440" r="380" fill="var(--blue-soft)" opacity="0.75"/>
      <circle class="ring-inner" cx="560" cy="440" r="308" fill="var(--blue-pale)"/>
      <rect class="info-band" x="0" y="321" width="330" height="206" fill="var(--white)"/>
      <circle class="portrait" cx="542" cy="442" r="248" fill="url(#photo-tone)"
              role="img" aria-label="Photo of a smiling young professional in a white shirt reviewing charts at an office desk"/>
    </svg>

    <h1 class="headline">Do you have an analytical mind and<br>seeking a profitable career?</h1>

    <p class="copy intro">A Master's in Business Analytics-<br>Ridgewell State University **</p>
    <p class="copy salary">can prepare you for in-demand jobs<br>with a median salary of $100k+</p>
    <p class="copy source">National Labor Data Office 2023</p>

    <ul class="band-list roles">
      <li>BI Developer</li>
      <li>Data Analyst</li>
      <li>Data Scientist</li>
      <li>Data Developer</li>
    </ul>

    <h2 class="hired-title">GRADUATES WERE HIRED AT:</h2>
    <ul class="band-list employers">
      <li>Norvane Health</li>
      <li>Kestrel Advisory</li>
      <li>Corvex Systems</li>
      <li>Voltaris Motors</li>
      <li>Harborline Insurance</li>
    </ul>

    <h2 class="open-house-title">OPEN HOUSE</h2>
    <p class="copy event">Wednesday, April 20, 7:30 pm<br>info@ridgewellmba.edu&nbsp; for the link!</p>

    <p class="copy accreditation">*** GBEA Accreditation. A distinction held by<br>only 5% of business schools globally.</p>

    <p class="program-facts">Men &amp; Women Program<br>21 months<br>Hybrid with one weekly in-person evening meeting</p>
  </article>
</main>
</body>
</html>
```